Landlord Handbook for real estate agency clients

We are a boutique Real Estate Agency that specializes in Property Management (Rentals) Located on Sydney's Northern Beaches.

We are putting together a property owners handbook that informs them about being a landlord, setting up their property for rent, local legislation on leasing properties, the services we offer and what makes us a great choice to manage their property.
Ultimately this is designed to answer new landlords FAQs and sell our agency as the best choice for them.

We want this handbook to be simple, clear and styled to match our existing website. wwww.harbourlinkrealty.com.au

We have supplied some images, screen shots of our Landlord Portal service offered. All words and index are provided in the word.doc
The services we want to feature are:
Our Landlord Portal
Our Service Guarantee
Quality Tenant Database
6 Month Property Reports

I would like the brochure to be around 16-20 A4 pages with some of the images provided and/or any other images you would like to add.

An example of a similar owners handbook can be found here: http://www.zentro.com.au/marsh_kettleby_poh/
But I would like something a little more modern and matched to our website design.

I would like a print ready PDF version of document as well as an editable Photoshop copy and AI copy.

Thank you and I look forward t your designs!
Tom.

Target Market(s)

30-65YO Men and women that own investment properties on Sydney's Northern Beaches

Industry/Entity Type

Real Estate

Font styles to use
Serif

Requirements
Must have
• Must use one of the Town house images provided on the front cover to match our website www.harbourlinkrealty.com.au
• Index of details at the start.
• Use one or all of our screen shot images of the Landlord Portal to promote this feature within the landlord portal description in content.
Should not have
• Any images of foreign currency, landscapes or houses. We are based in Sydney Australia on the beach so we want to keep it local and use Australian images, currency, landscapes and houses.

```html
<!DOCTYPE html>
<html lang="en">
<head>
<meta charset="utf-8">
<title>Harbourlink Realty – Landlord Handbook Cover</title>
<link rel="stylesheet" href="https://fonts.googleapis.com/css2?family=Oswald:wght@400;500;600&family=Tinos&family=Montserrat:wght@600;700&family=Arimo&display=swap">
<style>
  :root {
    --backdrop: #a9a9a9;
    --paper: #ffffff;
    --teal: #3a9ea5;
    --teal-deep: #2f6e76;
    --teal-head: #2b7f8c;
    --ink: #1e1e1e;
    --logo-ink: #2a2a2a;
    --sky: #8fc6e6;
    --leaf: #5f8a4a;
  }
  * { margin: 0; padding: 0; box-sizing: border-box; }
  html, body { width: 1200px; height: 978px; overflow: hidden; }
  body { background: var(--backdrop); position: relative; }

  .spread {
    position: absolute; left: 104px; top: 124px;
    width: 996px; height: 714px;
    background: var(--paper);
    box-shadow: 0 12px 24px rgba(0,0,0,.25);
  }
  .spread-shapes { position: absolute; inset: 0; }

  .brand-name {
    position: absolute;
    font-family: "Oswald", sans-serif; font-weight: 500;
    color: var(--logo-ink); letter-spacing: .5px;
    display: flex; align-items: center; gap: 8px;
    white-space: nowrap;
  }
  .brand-name .brand-dot {
    width: 12px; height: 12px; border-radius: 50%; background: var(--teal);
  }
  .brand-front { left: 521px; top: 40px; font-size: 30px; }
  .brand-back { left: 31px; top: 514px; font-size: 26px; }

  .team-heading {
    position: absolute; left: 31px; top: 216px;
    font-family: "Oswald", sans-serif; font-weight: 600;
    font-size: 24px; color: var(--teal-head); letter-spacing: .3px;
  }
  .team-copy {
    position: absolute; left: 31px; top: 258px; width: 238px;
    font-family: "Tinos", serif; font-size: 13px; line-height: 16.4px;
    color: var(--ink); text-align: justify;
  }

  .contact-list {
    position: absolute; left: 31px; top: 600px; list-style: none;
    color: var(--paper);
  }
  .contact-list li { display: flex; align-items: center; height: 24.5px; }
  .contact-list svg { width: 14px; height: 14px; margin-right: 18px; flex: none; }
  .contact-list .contact-text { font-family: "Arimo", sans-serif; font-size: 12px; }
  .contact-list .contact-phone {
    font-family: "Montserrat", sans-serif; font-weight: 700; font-size: 20px; letter-spacing: .5px;
  }
  .contact-list li:first-child { height: 32px; }

  .tagline {
    position: absolute; left: 651px; top: 596px;
    font-family: "Oswald", sans-serif; font-weight: 600; color: var(--teal-head);
    line-height: 1;
  }
  .tagline-top { display: block; font-size: 30px; letter-spacing: .2px; }
  .tagline-bottom { display: block; font-size: 36px; margin-top: 6px; color: var(--teal); }

  .front-web {
    position: absolute; left: 586px; top: 679px; width: 410px; height: 32px;
    display: flex; align-items: center; justify-content: center;
    font-family: "Montserrat", sans-serif; font-weight: 600; font-size: 14px;
    color: var(--paper); letter-spacing: .3px;
  }
  .front-web b { font-weight: 700; }
</style>
</head>
<body>
  <main class="spread">
    <svg class="spread-shapes" width="996" height="714" viewBox="0 0 996 714">
      <defs>
        <linearGradient id="townhouse-tones" x1="0" y1="0" x2="0" y2="1">
          <stop offset="0" stop-color="var(--sky)"/>
          <stop offset=".45" stop-color="#7f8a8e"/>
          <stop offset=".75" stop-color="var(--leaf)"/>
          <stop offset="1" stop-color="#9a9a96"/>
        </linearGradient>
      </defs>
      <!-- header bands, front cover -->
      <polygon points="758,94 780,94 760,131 738,131" fill="var(--teal-deep)"/>
      <polygon points="790,94 996,94 996,131 770,131" fill="var(--teal)"/>
      <!-- cover photograph area -->
      <polygon role="img" aria-label="Photo of modern terraced townhouses with landscaped gardens and stairs along a sunny street"
               points="471,131 996,131 996,573 356,573" fill="url(#townhouse-tones)"/>
      <!-- footer bands -->
      <polygon points="0,589 590,589 532,711 0,711" fill="var(--teal)"/>
      <polygon points="604,589 624,589 566,711 546,711" fill="var(--teal)"/>
      <polygon points="636,589 656,589 598,711 578,711" fill="var(--teal-deep)"/>
      <polygon points="598,679 996,679 996,711 583,711" fill="var(--teal-deep)"/>
    </svg>

    <div class="brand-name brand-front"><span class="brand-dot"></span>HARBOURLINK REALTY</div>

    <h2 class="team-heading">OUR BROAD TEAM:</h2>
    <p class="team-copy">Not only do we have a friendly, professional and efficient property management team – we also work closely with associated builders, accountants and mortgage brokers. So you have access to experienced professionals in all facets of property investment.We work for you and its in our best interest that you get the best advice and service possible to get the most out of your investment.</p>

    <div class="brand-name brand-back"><span class="brand-dot"></span>HARBOURLINK REALTY</div>

    <ul class="contact-list">
      <li>
        <svg viewBox="0 0 16 16" aria-hidden="true"><path fill="#fff" d="M2 4c0-1.5 3-3 6-3s6 1.5 6 3v1h-3V3.8C10 3.3 9 3 8 3s-2 .3-3 .8V5H2zM4 6h8l2 6v2H2v-2zm4 2a2 2 0 100 4 2 2 0 000-4z"/></svg>
        <span class="contact-phone">0400 555 218</span>
      </li>
      <li>
        <svg viewBox="0 0 16 16" aria-hidden="true"><path fill="#fff" d="M8 1a5 5 0 00-5 5c0 4 5 9 5 9s5-5 5-9a5 5 0 00-5-5zm0 7a2 2 0 110-4 2 2 0 010 4z"/></svg>
        <span class="contact-text">PO Box 742 Collaroy, NSW 2097</span>
      </li>
      <li>
        <svg viewBox="0 0 16 16" aria-hidden="true"><path fill="#fff" d="M1 3h14v10H1zm1.5 1.2L8 8.5l5.5-4.3z"/></svg>
        <span class="contact-text">referrals@harbourlinkrealty.com.au</span>
      </li>
      <li>
        <svg viewBox="0 0 16 16" aria-hidden="true"><g fill="none" stroke="#fff" stroke-width="1.3"><circle cx="8" cy="8" r="6.3"/><ellipse cx="8" cy="8" rx="2.7" ry="6.3"/><path d="M1.7 8h12.6M2.8 4.8h10.4M2.8 11.2h10.4"/></g></svg>
        <span class="contact-text">www.harbourlinkrealty.com.au</span>
      </li>
    </ul>

    <h1 class="tagline">
      <span class="tagline-top">PROPERTY MANAGEMENT</span>
      <span class="tagline-bottom">DONE RIGHT!</span>
    </h1>
    <div class="front-web">www.<b>harbourlinkrealty</b>.com.au</div>
  </main>
</body>
</html>
```